TR Stationery - Modern Contemporary

Develop modern template for Letterhead and Stationery (business card, letterhead, envelopes) using the TR Logo and Icon

Colors
0054AA
0677BA
7BADD7
CADEEF
E8F1F8
00AB8E
00BBA5
67D7C9
C6EFE9
E9F9F6
EE7325
F08F49
F5BC92
FAE3D3
FDF4ED
6B429C
8869AF
B7A5CE
E3DAEB
F3F0F8

```html
<!DOCTYPE html>
<html lang="en">
<head>
<meta charset="utf-8">
<title>Tera Rivo Stationery</title>
<link href="https://fonts.googleapis.com/css2?family=Open+Sans:wght@400;600;700&family=Mrs+Saint+Delafield&display=swap" rel="stylesheet">
<style>
  :root {
    --backdrop: #a0a0a0;
    --paper: #ffffff;
    --navy: #2b2f4c;
    --green: #2aa865;
    --orange: #ee7325;
    --ink: #3a3a3a;
    --ink-soft: #4a4a4a;
  }
  * { margin: 0; padding: 0; box-sizing: border-box; }
  html, body { width: 1200px; height: 808px; overflow: hidden; }
  body {
    background: var(--backdrop);
    font-family: "Open Sans", Arial, sans-serif;
    color: var(--ink);
    position: relative;
  }
  .piece { position: absolute; background: var(--paper); overflow: hidden; }
  .wordmark {
    font-family: "Open Sans", Arial, sans-serif;
    font-weight: 400;
    letter-spacing: 0.5px;
    line-height: 1;
    white-space: nowrap;
    color: var(--navy);
  }
  .wordmark.on-dark { color: #ffffff; }

  /* Business card back */
  .card-back { left: 115px; top: 54px; width: 256px; height: 146px; background: var(--navy); }
  .card-back .wordmark { position: absolute; left: 0; right: 0; top: 54px; text-align: center; font-size: 27px; }

  /* Business card front */
  .card-front { left: 360px; top: 95px; width: 256px; height: 146px; }
  .card-front .wordmark { position: absolute; left: 18px; top: 64px; font-size: 17px; }
  .card-front .divider { position: absolute; left: 131px; top: 38px; width: 1px; height: 70px; background: var(--navy); }
  .card-front .details { position: absolute; left: 140px; top: 37px; font-size: 6.3px; line-height: 9px; color: var(--ink-soft); }
  .card-front .person-name { font-size: 9px; font-weight: 700; color: var(--navy); line-height: 11px; letter-spacing: 0.2px; }
  .card-front .person-title { color: var(--green); font-size: 6.5px; margin-bottom: 5px; }
  .card-front .address { margin-bottom: 5px; }

  .contact-line { display: flex; align-items: center; gap: 3px; white-space: nowrap; }
  .contact-line svg { flex: none; }

  /* Envelope back */
  .envelope-back { left: 115px; top: 265px; width: 502px; height: 219px; }
  .envelope-back .wordmark { position: absolute; left: 16px; top: 11px; font-size: 22px; }
  .envelope-back .return-address { position: absolute; left: 16px; top: 187px; font-size: 6.8px; line-height: 9.5px; color: var(--ink-soft); }

  /* Envelope with flap */
  .envelope-flap { left: 115px; top: 518px; width: 502px; height: 220px; }
  .envelope-flap .flap { position: absolute; left: 0; top: 0; }
  .envelope-flap .wordmark { position: absolute; left: 0; right: 0; top: 22px; text-align: center; font-size: 27px; }

  /* Letterhead */
  .letterhead { left: 647px; top: 95px; width: 459px; height: 643px; }
  .letterhead .wordmark { position: absolute; left: 35px; top: 38px; font-size: 27px; }
  .letterhead .divider { position: absolute; left: 303px; top: 31px; width: 1px; height: 51px; background: var(--navy); }
  .letterhead .sender { position: absolute; left: 314px; top: 29px; font-size: 7.3px; line-height: 9.8px; color: var(--ink-soft); }
  .letterhead .sender .address { margin-bottom: 2px; }
  .recipient { position: absolute; left: 35px; top: 171px; color: var(--ink-soft); }
  .recipient-name { font-size: 8.8px; line-height: 12px; }
  .recipient-meta { font-size: 6.3px; line-height: 11px; }
  .letter-body { position: absolute; left: 35px; top: 227px; width: 389px; font-size: 6.1px; line-height: 11.2px; text-align: justify; color: var(--ink-soft); }
  .letter-body p { margin-bottom: 9.5px; }
  .closing { position: absolute; left: 35px; top: 405px; font-size: 7px; color: var(--ink-soft); }
  .signature { position: absolute; left: 35px; top: 414px; font-family: "Mrs Saint Delafield", cursive; font-size: 22px; color: #1c1c1c; }
</style>
</head>
<body>

  <section class="piece card-back" aria-label="Business card back">
    <div class="wordmark on-dark">tera rivo</div>
  </section>

  <section class="piece card-front" aria-label="Business card front">
    <div class="wordmark">tera rivo</div>
    <div class="divider"></div>
    <div class="details">
      <div class="person-name">TOM RELLER</div>
      <div class="person-title">President</div>
      <div class="address">1820 Harbor View Lane<br>Bay Cove CA 90000</div>
      <div class="contact-line">
        <svg width="6" height="6" viewBox="0 0 10 10"><path d="M2 1l2 2-1 1.5a6 6 0 0 0 2.5 2.5L7 6l2 2-1.5 1.5C4.5 9.5.5 5.5.5 2.5z" fill="var(--orange)"/></svg>
        <span>555-010-2468</span>
      </div>
      <div class="contact-line">
        <svg width="6" height="6" viewBox="0 0 10 10"><rect x="0.5" y="2" width="9" height="6" fill="var(--orange)"/><path d="M0.5 2l4.5 3.5L9.5 2" stroke="#fff" stroke-width="1" fill="none"/></svg>
        <span>treller@terarivo.com</span>
      </div>
      <div class="contact-line">
        <svg width="6" height="6" viewBox="0 0 10 10"><circle cx="5" cy="5" r="4.5" fill="var(--orange)"/><path d="M0.5 5h9M5 0.5v9" stroke="#fff" stroke-width="0.8"/></svg>
        <span>www.terarivo.com</span>
      </div>
    </div>
  </section>

  <section class="piece envelope-back" aria-label="Envelope back">
    <div class="wordmark">tera rivo</div>
    <div class="return-address">1820 Harbor View Lane<br>Bay Cove CA 90000</div>
  </section>

  <section class="piece envelope-flap" aria-label="Envelope with flap">
    <svg class="flap" width="502" height="78" viewBox="0 0 502 78">
      <path d="M0 0H502L492 45Q486 76 455 76H47Q16 76 10 45Z" fill="var(--navy)"/>
    </svg>
    <div class="wordmark on-dark">tera rivo</div>
  </section>

  <section class="piece letterhead" aria-label="Letterhead">
    <div class="wordmark">tera rivo</div>
    <div class="divider"></div>
    <div class="sender">
      <div class="address">1820 Harbor View Lane<br>Bay Cove CA 90000</div>
      <div class="contact-line">
        <svg width="7" height="7" viewBox="0 0 10 10"><path d="M2 1l2 2-1 1.5a6 6 0 0 0 2.5 2.5L7 6l2 2-1.5 1.5C4.5 9.5.5 5.5.5 2.5z" fill="var(--orange)"/></svg>
        <span>555-010-2468</span>
      </div>
      <div class="contact-line">
        <svg width="7" height="7" viewBox="0 0 10 10"><rect x="0.5" y="2" width="9" height="6" fill="var(--orange)"/><path d="M0.5 2l4.5 3.5L9.5 2" stroke="#fff" stroke-width="1" fill="none"/></svg>
        <span>treller@terarivo.com</span>
      </div>
      <div class="contact-line">
        <svg width="7" height="7" viewBox="0 0 10 10"><circle cx="5" cy="5" r="4.5" fill="var(--orange)"/><path d="M0.5 5h9M5 0.5v9" stroke="#fff" stroke-width="0.8"/></svg>
        <span>www.terarivo.com</span>
      </div>
    </div>

    <div class="recipient">
      <div class="recipient-name">TOMAS RELLER</div>
      <div class="recipient-meta">President / CEO</div>
      <div class="recipient-meta">City/State, Zip Code</div>
    </div>

    <div class="letter-body">
      <p>Lorem Ipsum is simply dummy text of the printing and typesetting industry. Lorem Ipsum has been the industry's standard dummy text ever since the 1500s, when an unknown printer took a galley of type and scrambled it to make a type specimen book. It has survived not only five centuries, but also the leap into electronic typesetting, remaining essentially unchanged. It was popularised in the 1960s with the release of transfer lettering sheets containing Lorem Ipsum passages, and more recently with desktop publishing software and page layout programs including versions of Lorem Ipsum.</p>
      <p>It is a long established fact that a reader will be distracted by the readable content of a page when looking at its layout. The point of using Lorem Ipsum is that it has a more-or-less normal distribution of letters, as opposed to using 'Content here, content here', making it look like readable English. Many desktop publishing packages and web page editors now use Lorem Ipsum as their default model text, and a search accident, sometimes on purpose (injected humour and the like).</p>
      <p>There are many variations of passages of Lorem Ipsum available, but the majority have suffered alteration in some form, by injected humour, or randomised words which don't look even slightly believable. If you are going to use a passage of Lorem Ipsum, you need to be sure there isn't anything embarrassing hidden in the middle of text.</p>
    </div>

    <div class="closing">Sincerely,</div>
    <div class="signature">Kara Doyle</div>
  </section>

</body>
</html>
```